Meridian Forum Flyer

We need a company flyer to present our company. Target group: Senior managers of hospitals / care facilities.
Please use the new text from the document "Kongressflyer.pptx".
Design: The last flyer can be used as a design basis - attached here: "Bright Orbit Flyer High Res Compressed.pdf". Please note the layout of the business card. The flyer must visually match the business card.
Logos for the references attached (KTW, Varmon, Chemnitz, Cologne, Am Lindenhain, Brückwerk, Tobe, PLMR).
Format: DIN A long in portrait format, front and back printed (or open to alternative suggestions if the format does not appear optimal from a design point of view)
Timing: We need the flyer as soon as possible

```html
<!DOCTYPE html>
<html lang="de">
<head>
<meta charset="utf-8">
<title>Bright Orbit Flyer</title>
<link href="https://fonts.googleapis.com/css2?family=Poppins:wght@400;600;700&display=swap" rel="stylesheet">
<style>
:root{
  --stage:#e4e4e6;
  --teal:#0f5566;
  --blue:#1a8fc9;
  --red:#e84a3c;
  --ink:#1d1d1f;
  --band-blue:#3b78c0;
  --white:#ffffff;
  --sky-deep:#8fcde3;
  --sky-mid:#bfe4ef;
  --sky-pale:#eef7fa;
}
*{margin:0;padding:0;box-sizing:border-box}
html,body{width:1200px;height:2182px;overflow:hidden;background:var(--stage);font-family:"Poppins",sans-serif;color:var(--ink)}
.flyer{position:absolute;left:46px;top:89px;width:1107px;height:1875px;overflow:hidden;background:linear-gradient(180deg,#e3f2f7 0%,#eef7fa 35%,#f0f7fa 100%)}
.flyer-header-art{position:absolute;left:0;top:0;width:100%;height:620px;
  background:
    radial-gradient(ellipse 420px 300px at 280px 120px,rgba(120,195,222,.55),rgba(120,195,222,0) 70%),
    radial-gradient(ellipse 360px 260px at 600px 60px,rgba(70,160,205,.45),rgba(70,160,205,0) 70%),
    radial-gradient(ellipse 420px 300px at 1000px 40px,rgba(110,190,220,.5),rgba(110,190,220,0) 70%),
    linear-gradient(180deg,var(--sky-mid) 0%,#d6eef5 45%,rgba(238,247,250,0) 100%)}
.abs{position:absolute;white-space:nowrap}
.brand-primary{left:137px;top:128px;font-size:33px;font-weight:400;letter-spacing:4px;color:var(--ink)}
.brand-partner{left:846px;top:112px;font-size:40px;font-weight:600;color:var(--teal)}
.intro{font-size:17px;line-height:22px}
.intro b{font-weight:700;color:var(--teal)}
.intro-lead{left:49px;top:342px}
.intro-item{left:116px}
.intro-cta{left:49px;top:499px;color:var(--blue);font-size:17.5px;line-height:22px}
.about-title{left:633px;top:388px;font-size:21px;font-weight:700;color:var(--teal)}
.about-text{left:633px;font-size:17px;line-height:26px}
.reasons-circle{position:absolute;left:-31px;top:580px;width:664px;height:664px;border-radius:50%;background:var(--red)}
.reasons{position:absolute;left:26px;width:560px;text-align:center;color:var(--white);font-size:17px;line-height:22px;font-weight:400}
.reasons.title{font-size:23px;line-height:34px;font-weight:700}
.reasons.point{font-weight:700;font-size:18px}
.ref-pill{left:636px;top:784px;width:202px;height:33px;border-radius:0 17px 17px 0;background:var(--teal);color:var(--white);font-size:22px;font-weight:700;text-align:center;line-height:33px}
.ref-name{font-size:22px;font-weight:700;color:var(--teal);text-align:center;width:190px;display:flex;align-items:center;justify-content:center;gap:8px}
.ref-name .dot{width:12px;height:12px;border-radius:50%;background:var(--teal)}
.positions-title{left:596px;top:1182px;font-size:25px;line-height:34px;font-weight:700;color:var(--red)}
.pos-head{left:596px;font-size:21px;font-weight:700;color:var(--teal)}
.pos-sub{left:596px;font-size:17.5px;line-height:22px;color:var(--ink);font-weight:400}
.pos-sub b{color:var(--blue);font-weight:700}
.pos-item{left:614px;font-size:17.5px}
.contact-photo{position:absolute;border-radius:4px;background:linear-gradient(180deg,#6b6b6b,#2a2a2a);box-shadow:0 1px 3px rgba(0,0,0,.3)}
.contact-photo.color{background:linear-gradient(180deg,#e9e4df,#7a6a60)}
.office{font-size:22px;font-weight:700;color:var(--teal)}
.person{font-size:18px;font-weight:600;color:var(--blue)}
.contact-line{font-size:18px}
.band-blue{position:absolute;left:0;top:1846px;width:100%;height:6px;background:var(--band-blue)}
.band-red{position:absolute;left:0;top:1859px;width:100%;height:16px;background:var(--red)}
</style>
</head>
<body>
<main class="flyer">
  <div class="flyer-header-art" role="img" aria-label="Helle blaue geometrische Dreiecksflächen als Hintergrundmuster"></div>

  <div class="abs brand-primary">BRIGHT ORBIT</div>
  <div class="abs brand-partner">Halvert</div>

  <p class="abs intro intro-lead">Sie sind Leiter eines Krankenhauses<br>und suchen...</p>
  <p class="abs intro intro-item" style="top:396px"><b>... medizinische Fachkräfte</b> für Ihre Klinik oder</p>
  <p class="abs intro intro-item" style="top:430px"><b>... herausragende Führungskräfte</b> für Ihre<br>&nbsp;&nbsp;&nbsp;&nbsp;Klinikverwaltung?</p>
  <p class="abs intro-cta">Möchten Sie dabei auf Augenhöhe begleitet<br>werden? Wir unterstützen Sie gerne.</p>

  <h2 class="abs about-title">Wer sind wir?</h2>
  <p class="abs about-text" style="top:426px">Seit fast 30 Jahren gehört das<br>Unternehmen Halvert / Bright Orbit zu<br>den bedeutensten Personalberatungen im<br>Gesundheitswesen. Die Rekrutierung von<br>Spitzenpersonal für Kliniken ist unsere<br>große Leidenschaft.</p>
  <p class="abs about-text" style="top:601px">Durch den Zusammenschluss der beiden<br>Firmen haben wir uns im letzten Jahr<br>modernisiert, digitalisiert und für die<br>Zukunft aufgestellt – ohne dabei die<br>Tradition aus den Augen zu verlieren.</p>

  <div class="reasons-circle"></div>
  <h2 class="reasons title" style="top:634px">Warum können wir Sie<br>bestmöglich unterstützen?</h2>
  <p class="reasons point" style="top:710px">• Ehrlichkeit ist uns wichtig ...</p>
  <p class="reasons" style="top:744px;left:10px;width:592px">... bei uns bekommen Sie aufrichtiges Marktfeedback und</p>
  <p class="reasons" style="top:778px;left:10px;width:592px">... garantiert keine Versprechungen, die wir nicht halten<br>können</p>
  <p class="reasons point" style="top:844px">• Wir lieben was wir tun ...</p>
  <p class="reasons" style="top:878px">... und wir arbeiten schnell, effizient und auf Augenhöhe</p>
  <p class="reasons point" style="top:922px">• Wir sind Spezialisten im Gesundheitswesen ...</p>
  <p class="reasons" style="top:956px">... unser Team verfügt über fundiertes Marktverständnis</p>
  <p class="reasons point" style="top:1000px">• Überragendes Netzwerk ...</p>
  <p class="reasons" style="top:1034px">... in allen Teilsektoren des Gesundheitswesens</p>
  <p class="reasons point" style="top:1078px">• Digital ...</p>
  <p class="reasons" style="top:1112px;left:40px">... unsere Prozesse? Transparent! Unsere Suche<br>für Sie 24/7 einsehbar</p>

  <div class="abs ref-pill">Referenzen</div>
  <div class="abs ref-name" style="left:661px;top:852px"><span class="dot"></span>Varmon</div>
  <div class="abs ref-name" style="left:875px;top:852px"><span class="dot"></span>KTW</div>
  <div class="abs ref-name" style="left:661px;top:937px">Tobe</div>
  <div class="abs ref-name" style="left:875px;top:937px;font-size:18px">Am Lindenhain</div>
  <div class="abs ref-name" style="left:661px;top:1013px;font-size:17px">Klinikum Feldau</div>
  <div class="abs ref-name" style="left:875px;top:1013px;font-size:17px">Uniklinik Rebach</div>
  <div class="abs ref-name" style="left:661px;top:1077px">PLMR</div>
  <div class="abs ref-name" style="left:875px;top:1077px"><span class="dot" style="border-radius:0"></span>Brückwerk</div>

  <h2 class="abs positions-title">Was sind typische Positionen,<br>die wir besetzen?</h2>

  <h3 class="abs pos-head" style="top:1288px">Medizinische Fachkräfte</h3>
  <p class="abs pos-sub" style="top:1315px"><b>&gt; 100 Besetzungen</b> in vergangenen 2 Jahren <b>in<br>sämtlichen Fachrichtungen,</b> z.B.</p>
  <p class="abs pos-item" style="top:1374px">• Chefarzt Gynäkologie / Geburtshilfe</p>
  <p class="abs pos-item" style="top:1413px">• Chefarzt Radiologie</p>
  <p class="abs pos-item" style="top:1452px">• Chefarzt Psychiatrie</p>

  <h3 class="abs pos-head" style="top:1520px">Herausragende Führungskräfte</h3>
  <p class="abs pos-sub" style="top:1548px"><b>&gt; 150 Besetzungen von Leitungspositionen in<br>sämtlichen Geschäftsbereichen in vergangenen 2<br>Jahren, z.B.</b></p>
  <p class="abs pos-item" style="top:1629px">• Klinik Geschäftsführung / Vorstände</p>
  <p class="abs pos-item" style="top:1668px">• Leitung Personal</p>
  <p class="abs pos-item" style="top:1707px">• Leitung Qualitäts- und Risikomanagement</p>
  <p class="abs pos-item" style="top:1746px">• Leitung Patientenmanagement</p>

  <div class="contact-photo" style="left:51px;top:1249px;width:114px;height:165px" role="img" aria-label="Schwarzweiß-Porträtfoto der Ansprechpartnerin Büro Hamburg"></div>
  <h3 class="abs office" style="left:182px;top:1253px">Büro Hamburg</h3>
  <p class="abs person" style="left:182px;top:1290px">Dr. med. Lena Hartwig Sommer</p>
  <p class="abs contact-line" style="left:182px;top:1323px">lhs@brightorbit.io</p>
  <p class="abs contact-line" style="left:182px;top:1356px">T: +49 170 5550142</p>

  <div class="contact-photo" style="left:51px;top:1468px;width:114px;height:165px" role="img" aria-label="Schwarzweiß-Porträtfoto der Ansprechpartnerin Büro Wien"></div>
  <h3 class="abs office" style="left:178px;top:1482px">Büro Wien</h3>
  <p class="abs person" style="left:178px;top:1519px">Clara Weinert</p>
  <p class="abs contact-line" style="left:178px;top:1552px">cw@brightorbit.io</p>
  <p class="abs contact-line" style="left:178px;top:1585px">T: +43 660 5550278</p>

  <div class="contact-photo color" style="left:42px;top:1685px;width:114px;height:161px" role="img" aria-label="Farbiges Porträtfoto der Ansprechpartnerin Büro Düsseldorf"></div>
  <h3 class="abs office" style="left:174px;top:1693px">Büro Düsseldorf</h3>
  <p class="abs person" style="left:174px;top:1730px">Ann Kathrin Rollberg</p>
  <p class="abs contact-line" style="left:174px;top:1763px">akr@brightorbit.io</p>
  <p class="abs contact-line" style="left:174px;top:1797px">T: +49 171 555 0393</p>

  <div class="band-blue"></div>
  <div class="band-red"></div>
</main>
</body>
</html>
```